New Business Card Design Project

Use the flyer uploaded and website www.brightoakbuilders.com for inspiration.
List Our Services on Backside of business cards
Martin Hollis
Harborline Renovations Inc.
Licensed General Contractors
858-471-9063

Contact Information for Business Card

Use the flyer uploaded and website www.brightoakbuilders.com for inspiration. List Our Services on Backside of business cards Martin Hollis Harborline Renovations Inc. Licensed General Contractors 858-471-9063

```html
<!DOCTYPE html>
<html lang="en">
<head>
<meta charset="utf-8">
<title>Harborline Renovations – Business Card</title>
<link href="https://fonts.googleapis.com/css2?family=Cinzel:wght@400;500&family=Poppins:wght@600&family=Roboto:wght@400&display=swap" rel="stylesheet">
<style>
  :root {
    --stage: #b3b3b3;
    --card-dark: #131313;
    --card-light: #f4f4f4;
    --brand-blue: #3a85c9;
    --alert-red: #e3232a;
    --ink-light: #ffffff;
    --ink-dark: #2b2b2b;
    --rule: #bdbdbd;
  }
  * { margin: 0; padding: 0; box-sizing: border-box; }
  html, body { width: 1093px; height: 1200px; overflow: hidden; }
  body { background: var(--stage); position: relative; font-family: "Roboto", sans-serif; }

  .card { position: absolute; left: 265px; width: 578px; height: 356px; border-radius: 24px; overflow: hidden; }
  .card--front { top: 226px; background: var(--card-dark); }
  .card--back { top: 621px; background: var(--card-light); }

  /* Front */
  .brand-block {
    position: absolute; left: 280px; width: 282px; top: 52px;
    display: flex; flex-direction: column; align-items: center;
  }
  .brand-mark {
    width: 82px; height: 82px; border-radius: 50%;
    border: 1.5px solid var(--ink-light);
  }
  .brand-name {
    margin-top: 16px; text-align: center; white-space: nowrap;
    font-family: "Cinzel", serif; font-weight: 400; font-size: 20px; letter-spacing: 0.5px;
    color: var(--ink-light);
  }
  .name-row {
    position: absolute; left: 32px; right: 35px; top: 190px;
    display: flex; align-items: center;
  }
  .person-name {
    font-family: "Cinzel", serif; font-weight: 500; font-size: 24px; color: var(--brand-blue);
    letter-spacing: 0.5px; white-space: nowrap;
  }
  .name-rule { flex: 1; height: 1px; margin-left: 12px; margin-top: 4px; background: var(--rule); }
  .contact-list { position: absolute; left: 30px; top: 253px; list-style: none; }
  .contact-list li {
    display: flex; align-items: center; height: 21px;
    font-size: 17px; color: var(--ink-light);
  }
  .contact-list svg { width: 16px; height: 16px; margin-right: 9px; fill: var(--brand-blue); }
  .company-block {
    position: absolute; right: 31px; top: 276px; text-align: right;
    font-size: 17px; line-height: 21px; color: var(--alert-red);
  }

  /* Back */
  .guarantee {
    position: absolute; left: 0; width: 100%; top: 65px; text-align: center;
    font-family: "Poppins", sans-serif; font-weight: 600; font-size: 23px; color: var(--alert-red);
    text-transform: uppercase;
  }
  .specialty-tag { position: absolute; left: 177px; top: 96px; width: 226px; height: 45px; }
  .specialty-tag svg { position: absolute; inset: 0; }
  .specialty-tag span {
    position: absolute; left: 23px; top: 9px; font-size: 23px; color: var(--ink-light);
  }
  .service-list { position: absolute; top: 194px; list-style: none; }
  .service-list--left { left: 25px; }
  .service-list--right { left: 322px; }
  .service-list li {
    position: relative; padding-left: 13px; height: 22px;
    font-size: 17px; color: var(--ink-dark);
  }
  .service-list li::before {
    content: ""; position: absolute; left: 0; top: 6px; width: 5px; height: 5px;
    border-radius: 50%; background: var(--brand-blue);
  }
</style>
</head>
<body>
  <section class="card card--front">
    <div class="brand-block">
      <div class="brand-mark"></div>
      <div class="brand-name">Harborline Renovations</div>
    </div>
    <div class="name-row">
      <div class="person-name">MARTIN HOLLIS</div>
      <div class="name-rule"></div>
    </div>
    <ul class="contact-list">
      <li>
        <svg viewBox="0 0 24 24"><path d="M6.6 10.8a15.1 15.1 0 0 0 6.6 6.6l2.2-2.2a1 1 0 0 1 1-.25 11.4 11.4 0 0 0 3.6.57 1 1 0 0 1 1 1V20a1 1 0 0 1-1 1A17 17 0 0 1 3 4a1 1 0 0 1 1-1h3.5a1 1 0 0 1 1 1c0 1.25.2 2.45.57 3.57a1 1 0 0 1-.25 1z"/></svg>
        858-471-9063
      </li>
      <li>
        <svg viewBox="0 0 24 24"><path d="M2 5h20v14H2z M2 5l10 8 10-8" fill="none" stroke="#3a85c9" stroke-width="2"/></svg>
        info@harborlinereno.com
      </li>
      <li>
        <svg viewBox="0 0 24 24"><g fill="none" stroke="#3a85c9" stroke-width="1.8"><circle cx="12" cy="12" r="9.5"/><ellipse cx="12" cy="12" rx="4.5" ry="9.5"/><path d="M2.5 12h19M4 7h16M4 17h16"/></g></svg>
        BrightOakBuilders.com
      </li>
    </ul>
    <div class="company-block">
      Harborline Renovations Inc<br>
      Licensed General Contractors
    </div>
  </section>

  <section class="card card--back">
    <h2 class="guarantee">Our services are 100% guarenteed</h2>
    <div class="specialty-tag">
      <svg viewBox="0 0 226 45" preserveAspectRatio="none"><polygon points="0,0 226,0 213,45 0,45" fill="#3a85c9"/></svg>
      <span>SPECIALIZING IN</span>
    </div>
    <ul class="service-list service-list--left">
      <li>Remodel: Kitchen &amp; Bath</li>
      <li>Painting: Interior &amp; Exterior</li>
      <li>Flooring: Carpet, Vinyl, Wood</li>
      <li>Window &amp; Door Replacement</li>
      <li>Plumbing: Repairs &amp; Upgrades</li>
    </ul>
    <ul class="service-list service-list--right">
      <li>Energy-Efficient Upgrades</li>
      <li>Deck &amp; Patio Construction</li>
      <li>Water &amp; Mold Damage</li>
      <li>Garage Renovation</li>
    </ul>
  </section>
</body>
</html>
```